Zelvo RT Biz Card Design

Residential / Commercial/ Emergency

Residential

Tomas Wexley
President
PO Box 4827
Marren Point, NY 10987
tomas@zelvo-rt.com
631.555.0187
844.ZELVO.RT
www.zelvo-rt.com
FB: Zelvo RT
Twitter: ZELVO RT

```html
<!DOCTYPE html>
<html lang="en">
<head>
<meta charset="UTF-8">
<title>Zelvo RT Business Card</title>
<link href="https://fonts.googleapis.com/css2?family=Oswald:wght@700&family=PT+Sans:wght@400&display=swap" rel="stylesheet">
<style>
  :root {
    --bg: #e4e6e5;
    --card-white: #f7f7f7;
    --card-dark: #23272b;
    --brand-orange: #e07b1a;
    --text-dark: #2a2a2a;
    --text-light: #f2f2f2;
    --art-sky: #dfe6e8;
    --art-green: #7d9a5a;
  }
  * { margin: 0; padding: 0; box-sizing: border-box; }
  html, body { width: 1200px; height: 900px; overflow: hidden; background: var(--bg); }
  .canvas { position: relative; width: 1200px; height: 900px; }

  .card {
    position: absolute;
    width: 560px;
    height: 320px;
    overflow: hidden;
    box-shadow: 0 10px 28px rgba(0,0,0,0.22);
  }

  /* Front */
  .card--front { left: 90px; top: 90px; background: var(--card-white); }
  .front-art {
    position: absolute;
    right: 40px; top: 22px;
    width: 210px; height: 118px;
    background: linear-gradient(160deg, var(--art-sky) 0%, #c9d3c4 45%, var(--art-green) 100%);
    border-radius: 4px;
  }
  .front-wordmark {
    position: absolute;
    left: 36px; bottom: 90px;
    font-family: 'Oswald', sans-serif;
    font-weight: 700;
    font-size: 78px;
    letter-spacing: 5px;
    line-height: 1;
    color: var(--brand-orange);
  }
  .front-band {
    position: absolute;
    left: 0; bottom: 0;
    width: 100%; height: 72px;
    background: var(--card-dark);
  }

  /* Back */
  .card--back { left: 550px; top: 490px; background: var(--card-white); display: flex; }
  .back-services {
    width: 225px;
    background: var(--card-dark);
    padding: 42px 0 0 30px;
    list-style: none;
    font-family: 'PT Sans', sans-serif;
    font-size: 17px;
    line-height: 23px;
    color: var(--text-light);
  }
  .back-services li::before {
    content: "\00D7";
    color: var(--brand-orange);
    margin-right: 8px;
  }
  .back-stripe {
    position: relative;
    width: 44px;
    background: var(--card-dark);
    border-right: 16px solid var(--brand-orange);
  }
  .back-wordmark {
    position: absolute;
    left: 50%; top: 50%;
    transform: translate(-50%, -50%) rotate(-90deg);
    font-family: 'Oswald', sans-serif;
    font-weight: 700;
    font-size: 40px;
    letter-spacing: 3px;
    color: var(--brand-orange);
    white-space: nowrap;
  }
  .back-info {
    flex: 1;
    position: relative;
    font-family: 'PT Sans', sans-serif;
    color: var(--text-dark);
  }
  .person { position: absolute; left: 48px; top: 96px; }
  .person-name { font-size: 22px; letter-spacing: 0.5px; }
  .person-title { font-size: 10px; color: var(--brand-orange); text-align: right; }
  .contact {
    position: absolute;
    left: 28px; bottom: 68px;
    font-size: 11.5px;
    line-height: 15px;
    font-style: normal;
  }
</style>
</head>
<body>
<div class="canvas">

  <section class="card card--front">
    <div class="front-art" role="img" aria-label="Illustration of a small aircraft surveying a green landscape"></div>
    <div class="front-wordmark">ZELVO-RT</div>
    <div class="front-band"></div>
  </section>

  <section class="card card--back">
    <ul class="back-services">
      <li>Aero Farming</li>
      <li>Cellular Towers</li>
      <li>Comm/Ind Security</li>
      <li>Construction</li>
      <li>Inspections</li>
      <li>Luxury Yachts</li>
      <li>Post Disaster Views</li>
      <li>Public Safety</li>
      <li>Search &amp; Rescue</li>
      <li>Surveys</li>
    </ul>
    <div class="back-stripe"><span class="back-wordmark">ZELVO-RT</span></div>
    <div class="back-info">
      <div class="person">
        <div class="person-name">Tomas Wexley</div>
        <div class="person-title">Owner/President</div>
      </div>
      <address class="contact">
        631.555.0187 844.ZELVO.RT<br>
        tomas@zelvo-rt.com<br>
        www.zelvo-rt.com<br>
        PO Box 4827 Marren Point, NY 10987
      </address>
    </div>
  </section>

</div>
</body>
</html>
```